HVAC&INSULATION Company. Need a website INSULATION targeted.

We are a new HVAC and Insulation company from Washington. (less then 1 year). we already have a website, design, logo etc.. our existing website is targeted for HVAC services.

*** I want to open a 2nd website with a similar design. same logo. same name almost (KESTREL VENT->KESTREL INSULATION)

- our current website is www.kestrelventco.com
i want the new website to be targeted for insulation services

```html
<!DOCTYPE html>
<html lang="en">
<head>
<meta charset="utf-8">
<title>Kestrel Insulation – Home Insulation Services</title>
<link href="https://fonts.googleapis.com/css2?family=Montserrat:wght@400;500;600;700;800;900&family=Open+Sans:wght@400;600;700&display=swap" rel="stylesheet">
<style>
:root{
  --blue:#1b8de3;
  --blue-dark:#1572c0;
  --ink:#262626;
  --text:#555;
  --grey-bg:#f1f1f1;
  --footer:#2c2c2c;
  --white:#fff;
  --star:#d32323;
}
*{box-sizing:border-box;margin:0;padding:0}
html,body{width:1200px;height:4972px;overflow:hidden}
body{position:relative;background:var(--white);font-family:"Open Sans",Arial,sans-serif;color:var(--text)}
.abs{position:absolute}
.head{font-family:"Montserrat",Arial,sans-serif;color:var(--ink);font-weight:800;letter-spacing:.5px}
.btn{position:absolute;background:var(--blue);color:var(--white);font-family:"Montserrat",Arial,sans-serif;font-weight:700;font-size:15px;text-align:center;letter-spacing:.5px}

/* header */
.site-header{position:absolute;left:0;top:0;width:1200px;height:83px;background:var(--white);z-index:3}
.brand{position:absolute;left:30px;top:14px;display:flex;align-items:center;gap:12px}
.brand-dot{width:56px;height:56px;border-radius:50%;background:var(--blue)}
.brand-name{font-family:"Montserrat",Arial,sans-serif;font-weight:800;font-size:22px;color:var(--ink);white-space:nowrap}
.nav{position:absolute;right:30px;top:26px;display:flex;gap:8px;align-items:center}
.nav a{font-family:"Montserrat",Arial,sans-serif;font-size:14px;font-weight:600;color:var(--ink);text-decoration:none;padding:6px 10px;white-space:nowrap}
.nav a.active{border:2px solid var(--blue);color:var(--blue)}
.nav a.quote{background:var(--blue);color:var(--white);padding:8px 14px}

/* hero */
.hero{position:absolute;left:0;top:83px;width:1200px;height:553px;background:linear-gradient(100deg,#9aa6ae 0%,#c7cdd0 30%,#8d9aa3 55%,#eef1f2 100%)}
.hero-title{position:absolute;left:636px;top:96px;font-size:48px;color:var(--ink);white-space:nowrap}
.hero-sub{position:absolute;left:638px;top:150px;font-family:"Montserrat",Arial,sans-serif;font-size:28px;color:var(--ink);font-weight:500;white-space:nowrap}
.hero-call{position:absolute;left:646px;top:209px;width:242px;height:56px;background:var(--blue);color:var(--white);display:flex;align-items:center;gap:12px;padding-left:18px}
.hero-call small{display:block;font-size:11px;font-weight:700}
.hero-call b{font-family:"Montserrat",Arial,sans-serif;font-size:20px}
.dots{position:absolute;left:545px;top:500px;display:flex;gap:14px}
.dots i{width:8px;height:8px;border-radius:50%;background:var(--white);opacity:.8}

/* services */
.services{position:absolute;left:0;top:636px;width:1200px;height:978px;background:var(--grey-bg)}
.ghost{position:absolute;left:0;width:1200px;top:30px;text-align:center;font-family:"Montserrat",Arial,sans-serif;font-weight:900;font-size:170px;color:#e1e1e1;letter-spacing:4px}
.svc-intro{position:absolute;left:156px;top:153px;width:291px;height:511px;background:var(--blue);padding:50px 36px;color:var(--white)}
.svc-intro h2{font-family:"Montserrat",Arial,sans-serif;font-size:24px;font-weight:800}
.svc-intro hr{border:0;border-top:2px solid var(--white);width:60px;margin:14px 0 18px}
.svc-intro p{font-family:"Montserrat",Arial,sans-serif;font-size:19px;line-height:1.35;font-weight:500}
.svc-intro .all{display:inline-block;margin-top:30px;background:#4a4a4a;padding:14px 18px;font-size:13px;font-weight:700;font-family:"Montserrat",Arial,sans-serif}
.tile{position:absolute;overflow:hidden}
.tile .photo{position:absolute;inset:0}
.tile .label{position:absolute;left:20px;bottom:16px;color:var(--white);font-family:"Montserrat",Arial,sans-serif;font-weight:800;font-size:18px;line-height:1.1}
.tile .more{position:absolute;right:14px;bottom:16px;border:1px solid var(--white);background:var(--blue);color:var(--white);font-size:10px;font-weight:700;padding:5px 10px}

/* who */
.who-photo{position:absolute;left:151px;top:1680px;width:380px;height:380px;border-radius:50%;background:linear-gradient(135deg,#e9e5df,#b9a894 60%,#6b4a35)}
.who-bite{position:absolute;left:151px;top:1680px;width:380px;height:380px}
.who{position:absolute;left:587px;top:1700px;width:470px}
.accent{width:70px;height:4px;background:var(--blue);margin-bottom:14px}
.who h2{font-size:26px}
.who p{font-size:15px;line-height:1.6;margin-top:18px}
.who .btn{position:relative;display:inline-block;margin-top:26px;padding:11px 18px;font-size:13px}

/* reviews */
.reviews{position:absolute;left:0;top:2138px;width:1200px;height:614px;background:var(--grey-bg)}
.reviews .accent{position:absolute;left:565px;top:64px}
.reviews h2{position:absolute;left:0;width:1200px;top:92px;text-align:center;font-size:30px}
.card{position:absolute;top:169px;width:292px;height:293px;background:var(--white);padding:26px 28px;box-shadow:0 2px 6px rgba(0,0,0,.05)}
.stars{display:flex;gap:3px}
.stars span{width:17px;height:17px;background:var(--star);display:flex;align-items:center;justify-content:center}
.card p{font-size:12.5px;line-height:1.55;margin-top:14px;color:#444}
.card .rm{display:block;font-size:11px;font-weight:700;color:var(--blue);margin-top:10px}
.card .who-by{position:absolute;left:28px;bottom:26px;display:flex;align-items:center;gap:12px;font-size:13px;font-weight:600;color:#333}
.card .who-by i{width:34px;height:34px;border-radius:50%;background:#c9c9c9}
.reviews .btn{left:510px;top:514px;width:180px;height:36px;line-height:36px;font-size:13px}

/* guarantee */
.guarantee{position:absolute;left:0;top:2752px;width:1200px;height:450px;overflow:hidden}
.guarantee h2{position:absolute;left:697px;top:100px;color:var(--white);font-size:44px;line-height:1.05}
.guarantee .band-text{position:absolute;left:718px;top:228px;color:var(--white);font-family:"Montserrat",Arial,sans-serif;font-weight:700;font-size:20px}
.guarantee p{position:absolute;left:672px;top:312px;width:420px;color:var(--white);font-size:18px;line-height:1.5}

/* love */
.love h2{position:absolute;left:0;width:1200px;text-align:center;top:3262px;font-size:29px;line-height:1.25}
.love .rule{position:absolute;left:392px;width:416px;height:1px;background:#cfcfcf}
.love p{position:absolute;left:0;width:1200px;text-align:center;top:3374px;font-size:15px;color:#333}
.badge{position:absolute;top:3454px;width:212px;height:113px;background:var(--white);box-shadow:0 2px 10px rgba(0,0,0,.12);display:flex;align-items:center;justify-content:center}

/* newsletter */
.newsletter-photo{position:absolute;left:0;top:3646px;width:1200px;height:604px;background:linear-gradient(100deg,#6b4f34,#caa57a 35%,#e6d3b1 55%,#b88a54 80%,#5d4027)}
.nl-box{position:absolute;left:398px;top:3719px;width:411px;height:392px;background:rgba(255,255,255,.93);text-align:center;padding:40px 40px 0}
.nl-box h3{font-size:21px;line-height:1.3}
.nl-box hr{border:0;border-top:1px solid #ccc;margin:14px 20px}
.nl-box p{font-size:16px;line-height:1.4;color:#333}
.field{margin-top:16px;height:46px;border:1px solid #888;background:var(--white);text-align:left;padding-left:14px;line-height:44px;font-size:12px;font-weight:700;color:#333}
.nl-box .btn{position:relative;display:block;margin-top:20px;height:46px;line-height:46px;font-size:16px}

.quote-box{position:absolute;left:312px;top:4193px;width:576px;height:299px;background:var(--white);box-shadow:0 4px 18px rgba(0,0,0,.14);text-align:center;padding-top:58px}
.quote-box h2{font-size:29px}
.quote-box .sub{font-family:"Montserrat",Arial,sans-serif;font-size:23px;color:#333;margin-top:6px;font-weight:500}
.quote-box .btn{left:128px;top:170px;width:320px;height:46px;line-height:46px;font-size:16px}

/* footer */
.footer{position:absolute;left:0;top:4575px;width:1200px;height:397px;background:var(--footer);overflow:hidden;color:#ddd}
.footer h4{font-family:"Montserrat",Arial,sans-serif;font-size:13px;font-weight:700;color:var(--white);letter-spacing:.5px}
.fcol{position:absolute;top:70px}
.fcol ul{list-style:none;margin-top:22px;font-size:12px;line-height:1.5;font-family:"Montserrat",Arial,sans-serif}
.crow{display:flex;align-items:center;gap:14px;margin-top:24px}
.crow i{width:28px;height:28px;border-radius:50%;background:#444;display:flex;align-items:center;justify-content:center;flex:none}
.crow small{display:block;font-size:10px;font-weight:700;color:var(--white)}
.crow b{font-family:"Montserrat",Arial,sans-serif;font-size:14px;font-weight:600;color:var(--white);white-space:nowrap}
.soc{display:flex;align-items:center;gap:10px;margin-top:16px;font-size:12px}
.soc i{width:22px;height:22px;border-radius:50%;background:var(--blue)}
.copy{position:absolute;left:0;width:1200px;bottom:56px;text-align:center;font-size:11px;color:#aaa}
.foot-brand{position:absolute;left:120px;top:70px;width:230px;text-align:center}
.foot-brand i{display:block;margin:0 auto;width:150px;height:150px;border-radius:50%;background:var(--white)}
.foot-brand span{display:block;margin-top:12px;font-family:"Montserrat",Arial,sans-serif;font-weight:800;font-size:15px;color:var(--white);white-space:nowrap}
</style>
</head>
<body>

<svg width="0" height="0" class="abs" aria-hidden="true">
  <symbol id="star" viewBox="0 0 10 10"><path fill="#fff" d="M5 .5l1.4 2.9 3.1.4-2.3 2.2.6 3.1L5 7.6 2.2 9.1l.6-3.1L.5 3.8l3.1-.4z"/></symbol>
  <symbol id="phone" viewBox="0 0 24 24"><path fill="#fff" d="M6.6 10.8a15 15 0 006.6 6.6l2.2-2.2c.3-.3.7-.4 1-.2 1.1.4 2.3.6 3.6.6.6 0 1 .4 1 1V20c0 .6-.4 1-1 1A17 17 0 013 4c0-.6.4-1 1-1h3.5c.6 0 1 .4 1 1 0 1.3.2 2.5.6 3.6.1.3 0 .7-.2 1z"/></symbol>
</svg>

<header class="site-header">
  <div class="brand"><span class="brand-dot"></span><span class="brand-name">KESTREL INSULATION</span></div>
  <nav class="nav">
    <a class="active">HOME</a><a>OUR TEAM</a><a>SERVICES</a><a>REVIEWS</a><a>SAVINGS &amp; SPECIALS</a><a class="quote">GET A QUOTE</a>
  </nav>
</header>

<section class="hero">
  <div class="abs" role="img" aria-label="Installer fitting insulation batts in an attic" style="inset:0"></div>
  <h1 class="hero-title head">HOME INSULATION</h1>
  <div class="hero-sub">WE KEEP YOUR HOME COMFORTABLE</div>
  <div class="hero-call">
    <svg width="26" height="26"><use href="#phone"/></svg>
    <div><small>CALL US</small><b>(555) 014-2290</b></div>
  </div>
  <div class="dots"><i></i><i></i><i></i><i></i><i></i></div>
</section>

<section class="services">
  <div class="ghost">SERVICES</div>
  <div class="svc-intro">
    <h2>OUR SERVICES</h2><hr>
    <p>INSULATING<br>SEALING &amp;<br>SAVING ENERGY</p>
    <span class="all">VIEW ALL SERVICES</span>
  </div>

  <div class="tile" style="left:457px;top:153px;width:285px;height:253px">
    <div class="photo" role="img" aria-label="Blown-in insulation in an attic" style="background:linear-gradient(160deg,#c9b79c,#a38a68 50%,#5e4b36)"></div>
    <div class="label">ATTIC</div><div class="more">READ MORE</div></div>
  <div class="tile" style="left:752px;top:153px;width:289px;height:253px">
    <div class="photo" role="img" aria-label="Insulation batts between wall studs" style="background:linear-gradient(160deg,#e2c9a8,#b39270 50%,#6a5440)"></div>
    <div class="label">WALLS</div><div class="more">READ MORE</div></div>
  <div class="tile" style="left:457px;top:416px;width:285px;height:248px">
    <div class="photo" role="img" aria-label="Wrapped air ducts with insulation" style="background:linear-gradient(160deg,#5c6166,#b7bcc0 50%,#3a3e42)"></div>
    <div class="label">DUCT WRAP</div><div class="more">READ MORE</div></div>
  <div class="tile" style="left:752px;top:416px;width:289px;height:248px">
    <div class="photo" role="img" aria-label="Worker applying spray foam" style="background:linear-gradient(160deg,#e6dfc9,#b9ad8c 55%,#5f5a4c)"></div>
    <div class="label">SPRAY FOAM</div><div class="more">READ MORE</div></div>
  <div class="tile" style="left:156px;top:677px;width:291px;height:252px">
    <div class="photo" role="img" aria-label="Insulated crawl space under a house" style="background:linear-gradient(160deg,#d4d1cc,#8f8a82 50%,#4f4a44)"></div>
    <div class="label">CRAWL SPACE</div><div class="more">READ MORE</div></div>
  <div class="tile" style="left:457px;top:677px;width:285px;height:252px">
    <div class="photo" role="img" aria-label="Sealing air leaks around a window" style="background:linear-gradient(160deg,#eef0f1,#bfc4c7 55%,#6f767b)"></div>
    <div class="label">AIR<br>SEALING</div><div class="more">READ MORE</div></div>
  <div class="tile" style="left:752px;top:677px;width:289px;height:252px">
    <div class="photo" role="img" aria-label="Installer fitting insulation in a wall" style="background:linear-gradient(160deg,#b08a61,#7d6248 50%,#3d3128)"></div>
    <div class="label">REMOVAL</div><div class="more">READ MORE</div></div>
</section>

<div class="who-photo" role="img" aria-label="Bright living room with a lit fireplace"></div>
<svg class="who-bite" viewBox="0 0 380 380"><path d="M190 190 L380 190 A190 190 0 0 1 190 380 Z" fill="#1b8de3" opacity=".85"/></svg>
<section class="who">
  <div class="accent"></div>
  <h2 class="head">WHO WE ARE</h2>
  <p>Kestrel Insulation is a local and family owned company. We provide high quality insulation services with excellent customer satisfaction in the greater Everett, WA area.</p>
  <p>We help families keep their homes warm in winter and cool in summer, and reduce their energy bills. We're committed to being a company and service that you trust.</p>
  <span class="btn">READ MORE</span>
</section>

<section class="reviews">
  <div class="accent"></div>
  <h2 class="head">OUR REVIEWS</h2>
  <svg class="abs" style="left:76px;top:298px" width="16" height="26" viewBox="0 0 16 26"><path d="M14 2L3 13l11 11" fill="none" stroke="#999" stroke-width="2"/></svg>
  <svg class="abs" style="left:1108px;top:298px" width="16" height="26" viewBox="0 0 16 26"><path d="M2 2l11 11L2 24" fill="none" stroke="#999" stroke-width="2"/></svg>

  <article class="card" style="left:139px">
    <div class="stars"><span><svg width="11" height="11"><use href="#star"/></svg></span><span><svg width="11" height="11"><use href="#star"/></svg></span><span><svg width="11" height="11"><use href="#star"/></svg></span><span><svg width="11" height="11"><use href="#star"/></svg></span><span><svg width="11" height="11"><use href="#star"/></svg></span></div>
    <p>5 star service! Our attic had almost no insulation left after 30 years. The crew topped it up in a single day, cleaned up after themselves and our upstairs rooms finally stay warm all winter long</p>
    <span class="rm">READ MORE</span>
    <div class="who-by"><i></i>Mukilteo, WA</div>
  </article>
  <article class="card" style="left:454px">
    <div class="stars"><span><svg width="11" height="11"><use href="#star"/></svg></span><span><svg width="11" height="11"><use href="#star"/></svg></span><span><svg width="11" height="11"><use href="#star"/></svg></span><span><svg width="11" height="11"><use href="#star"/></svg></span><span><svg width="11" height="11"><use href="#star"/></svg></span></div>
    <p>Our heating bills were climbing every year so we asked for an energy check. They found gaps in the walls and crawl space, sealed everything and added new insulation. Our last bill dropped by nearly a third ...</p>
    <span class="rm">READ MORE</span>
    <div class="who-by"><i></i>Dana R Marysville, WA</div>
  </article>
  <article class="card" style="left:766px">
    <div class="stars"><span><svg width="11" height="11"><use href="#star"/></svg></span><span><svg width="11" height="11"><use href="#star"/></svg></span><span><svg width="11" height="11"><use href="#star"/></svg></span><span><svg width="11" height="11"><use href="#star"/></svg></span><span><svg width="11" height="11"><use href="#star"/></svg></span></div>
    <p>Kestrel Insulation has earned not only my business but my trust. They weren't the first company I called but they are the best. Fair price, clear advice and the house is quieter and cozier......</p>
    <span class="rm">READ MORE</span>
    <div class="who-by"><i></i>Mukilteo, WA</div>
  </article>
  <span class="btn">VIEW ALL REVIEWS</span>
</section>

<section class="guarantee">
  <div class="abs" role="img" aria-label="Smiling installer holding insulation tools" style="left:0;top:0;width:760px;height:450px;background:linear-gradient(90deg,#8a7f74,#c9bfb4 40%,#5b4d45 75%,#2a2a2a)"></div>
  <svg class="abs" style="left:0;top:0" width="1200" height="450" viewBox="0 0 1200 450">
    <polygon points="640,0 1200,0 1200,450 560,450" fill="#1b8de3"/>
    <polygon points="600,208 1200,208 1200,266 586,266" fill="#1572c0"/>
  </svg>
  <h2 class="head">OUR<br>GUARANTEE</h2>
  <div class="band-text">WE TAKE PRIDE IN OUR WORK.</div>
  <p>That is why we offer a 100% satisfaction guarantee on every project!</p>
</section>

<section class="love">
  <h2 class="head">WE LOVE OUR CUSTOMERS<br>AND OUR CUSTOMERS LOVE US!</h2>
  <div class="rule" style="top:3350px"></div>
  <p>LEARN MORE ABOUT OUR HAPPY CUSTOMERS ON:</p>
  <div class="rule" style="top:3418px"></div>
  <div class="badge" style="left:146px"><svg width="60" height="60"><rect width="60" height="60" fill="#c9c9c9"/></svg></div>
  <div class="badge" style="left:371px"><svg width="80" height="80"><circle cx="40" cy="40" r="38" fill="#1b8de3"/></svg></div>
  <div class="badge" style="left:607px"><svg width="80" height="80"><rect width="80" height="80" fill="#1d5f99"/></svg></div>
  <div class="badge" style="left:835px"><svg width="70" height="70"><circle cx="35" cy="35" r="33" fill="#c9c9c9"/></svg></div>
</section>

<div class="newsletter-photo" role="img" aria-label="Warm living room with fireplace and armchairs"></div>
<section class="nl-box">
  <h3 class="head">GET 1 EMAIL EVERY<br>3 MONTHS &amp; SAVE MONEY!</h3>
  <hr>
  <p>Save up to 50% off. We promise,<br>ONE email every three months.</p>
  <div class="field">FULL NAME</div>
  <div class="field">E-MAIL ID</div>
  <span class="btn">I'D LOVE TO SAVE</span>
</section>

<section class="quote-box">
  <h2 class="head">GET A QUOTE FAST</h2>
  <div class="sub">WE RESPOND WITHIN 24 HOURS</div>
  <span class="btn">I'M READY FOR A QUOTE</span>
</section>

<footer class="footer">
  <svg class="abs" style="left:0;top:0" width="360" height="397" viewBox="0 0 360 397"><path d="M0 0 H40 C60 140 150 300 360 397 H0 Z" fill="#1b8de3"/></svg>
  <div class="foot-brand"><i></i><span>KESTREL INSULATION</span></div>
  <div class="fcol" style="left:398px">
    <h4>CONTACT US</h4>
    <div class="crow"><i><svg width="14" height="14"><use href="#phone"/></svg></i><div><small>CALL US</small><b>(555) 014-2290</b></div></div>
    <div class="crow"><i><svg width="14" height="12" viewBox="0 0 14 12"><rect x=".5" y=".5" width="13" height="11" fill="none" stroke="#fff"/><path d="M.5 .5l6.5 6 6.5-6" fill="none" stroke="#fff"/></svg></i><div><small>E-MAIL US</small><b>HELLO@KESTRELINSULATION.COM</b></div></div>
  </div>
  <div class="fcol" style="left:756px">
    <h4>MENU</h4>
    <ul><li>HOME</li><li>OUR TEAM</li><li>SERVICES</li><li>REVIEWS</li><li>SAVINGS &amp; SPECIALS</li><li>CONTACT US</li></ul>
  </div>
  <div class="fcol" style="left:950px">
    <h4>CONNECT WITH US</h4>
    <div class="soc" style="margin-top:22px"><i></i>Friendlink</div>
    <div class="soc"><i></i>Chirper</div>
    <div class="soc"><i></i>WorkNet</div>
  </div>
  <div class="copy">Copyrights © 2018 All Rights Reserved</div>
</footer>

</body>
</html>
```